Pale Harbor - post rock band album cover design

We are Pale Harbor, a post-rock band based on San Jose, CA, USA. We will release a new album “Where the rivers fold" and need a album cover.

The new album is full of emotion and energy. song list:
1. Forward
2. Search (in uploaded files)
3. Before
4. Memory
5. Dream
6. Spring
7. Om Namah Shivaya

Please hear our previous music here
https://pale-harbor.tunecrate-demo.net/album/pale-harbor

Target Market(s)

music lovers

Industry/Entity Type

Music Download

Colors

Requirements
Must have
• album cover + back
• For cover we only need band name (do not need album name), want to use some streamline font for the band name "Pale Harbor"
• I attached an example from another band
Nice to have
• I don't want to limit the designers, so please listen to the music and design what you feel the best:)

```html
<!DOCTYPE html>
<html lang="en">
<head>
<meta charset="utf-8">
<title>Pale Harbor — Album Cover and Back</title>
<link rel="stylesheet" href="https://fonts.googleapis.com/css2?family=Jost:wght@300&display=swap">
<style>
  :root {
    --stage: #0c0b0d;
    --ink: #f1f0f2;
    --ink-soft: rgba(241, 240, 242, 0.82);
    --rule: rgba(241, 240, 242, 0.45);
    --aurora-green: #3f6f5c;
    --aurora-teal: #2c4a48;
    --aurora-violet: #4f3d5e;
    --aurora-pink: #b3465f;
    --night: #101317;
    --ground: #07080a;
  }
  * { box-sizing: border-box; margin: 0; padding: 0; }
  html, body {
    width: 1200px;
    height: 521px;
    overflow: hidden;
    background: var(--stage);
  }
  .stage {
    position: relative;
    width: 1200px;
    height: 521px;
    display: flex;
    justify-content: center;
    align-items: center;
    gap: 44px;
    font-family: "Jost", "Futura", sans-serif;
    font-weight: 300;
    color: var(--ink);
  }
  .sleeve {
    position: relative;
    width: 410px;
    height: 410px;
    overflow: hidden;
  }
  .sleeve__photo {
    position: absolute;
    inset: 0;
    background:
      radial-gradient(ellipse 55% 35% at 12% 88%, var(--aurora-pink) 0%, transparent 70%),
      radial-gradient(ellipse 45% 30% at 30% 68%, var(--aurora-violet) 0%, transparent 75%),
      radial-gradient(ellipse 60% 40% at 55% 25%, var(--aurora-green) 0%, transparent 70%),
      radial-gradient(ellipse 50% 45% at 20% 30%, var(--aurora-teal) 0%, transparent 75%),
      linear-gradient(180deg, var(--night) 0%, #1b2325 55%, var(--ground) 100%);
  }
  .sleeve__photo::after {
    content: "";
    position: absolute;
    left: 0; right: 0; bottom: 0;
    height: 16%;
    background: linear-gradient(180deg, transparent 0%, var(--ground) 55%);
  }
  .cover__name {
    position: absolute;
    right: 34px;
    bottom: 88px;
    font-size: 24px;
    letter-spacing: 0.04em;
    color: var(--ink);
  }
  .back__content {
    position: absolute;
    inset: 0;
    display: flex;
    flex-direction: column;
    align-items: center;
  }
  .back__name {
    margin-top: 42px;
    font-size: 26px;
    letter-spacing: 0.04em;
    color: var(--ink);
  }
  .back__rule {
    width: 150px;
    height: 1px;
    background: var(--rule);
  }
  .back__rule--top { margin-top: 28px; }
  .tracklist {
    list-style: none;
    margin: 16px 0 14px;
    text-align: center;
  }
  .tracklist__item {
    font-size: 15.5px;
    line-height: 26.5px;
    letter-spacing: 0.06em;
    color: var(--ink-soft);
  }
</style>
</head>
<body>
<main class="stage">
  <section class="sleeve cover" aria-label="Album front cover">
    <div class="sleeve__photo" role="img" aria-label="Night photograph of green and violet northern lights over a dark treeline, with a pink glow on the horizon and a lone figure silhouetted in the foreground"></div>
    <p class="cover__name">Pale Harbor</p>
  </section>

  <section class="sleeve back" aria-label="Album back cover">
    <div class="sleeve__photo" role="img" aria-label="Night photograph of northern lights in green, violet and pink above a dark horizon"></div>
    <div class="back__content">
      <p class="back__name">Pale Harbor</p>
      <div class="back__rule back__rule--top"></div>
      <ol class="tracklist">
        <li class="tracklist__item">01. Forward</li>
        <li class="tracklist__item">02. Search</li>
        <li class="tracklist__item">03. Before</li>
        <li class="tracklist__item">04. Memory</li>
        <li class="tracklist__item">05. Dream</li>
        <li class="tracklist__item">06. Spring</li>
        <li class="tracklist__item">07.&nbsp; Om Namah Shivaya</li>
      </ol>
      <div class="back__rule"></div>
    </div>
  </section>
</main>
</body>
</html>
```